Kivo Commercial Cleaning is lookong for a new business card design.

A fresh new design that's professional and stylish. We need a serious upgrade to our business cards. I have included pictures of our existing ones. Our clients include professional individuals and business owners. We woupdblike something professional and upbeat. Please have fun and see what you come uo with.

Target Market(s)

Property managers, business owners, facility managers and other similar professionals

Industry/Entity Type

Janitorial

Contact Information for Business Card

Name, cell, office number, email, web address

Font styles to use
Sans Serif

Colors

Designer to choose colors to be used in the design.

Requirements
Must have
• please use the green color in our logo
Nice to have
• Bar code
Should not have
• Address

```html
<!DOCTYPE html>
<html lang="en">
<head>
<meta charset="utf-8">
<title>Kivo Commercial Cleaning — Business Card</title>
<link href="https://fonts.googleapis.com/css2?family=Lato:wght@700&family=Roboto:wght@300&display=swap" rel="stylesheet">
<style>
  :root {
    --kivo-green: #37b553;
    --card-white: #ffffff;
    --ink-grey: #555a5e;
    --backdrop: #8f8f8f;
    --shadow: rgba(0, 0, 0, 0.28);
  }
  * { margin: 0; padding: 0; box-sizing: border-box; }
  html, body { width: 1067px; height: 1200px; overflow: hidden; }
  body {
    background: var(--backdrop);
    display: flex;
    flex-direction: column;
    align-items: center;
    justify-content: center;
    gap: 80px;
  }
  .card {
    width: 700px;
    height: 400px;
    position: relative;
    box-shadow: 0 14px 30px var(--shadow);
    overflow: hidden;
  }

  /* Front */
  .card-front { background: var(--card-white); }
  .edge-band {
    position: absolute;
    left: 0; right: 0;
    height: 36px;
    background: var(--kivo-green);
  }
  .edge-band--top { top: 0; }
  .edge-band--bottom { bottom: 0; }
  .edge-rule {
    position: absolute;
    left: 0; right: 0;
    height: 2px;
    background: var(--kivo-green);
  }
  .edge-rule--top { top: 40px; }
  .edge-rule--bottom { bottom: 40px; }

  .brand-name {
    position: absolute;
    left: 44px;
    top: 138px;
    font-family: "Lato", sans-serif;
    font-weight: 700;
    font-size: 104px;
    line-height: 1;
    color: var(--kivo-green);
  }
  .divider {
    position: absolute;
    left: 348px;
    top: 128px;
    width: 2px;
    height: 148px;
    background: var(--kivo-green);
  }
  .contact {
    position: absolute;
    left: 380px;
    top: 124px;
  }
  .contact-name {
    font-family: "Lato", sans-serif;
    font-weight: 700;
    font-size: 38px;
    color: var(--kivo-green);
    margin-bottom: 18px;
    letter-spacing: -0.3px;
  }
  .contact-list { list-style: none; }
  .contact-item {
    display: flex;
    align-items: center;
    gap: 12px;
    font-family: "Roboto", sans-serif;
    font-weight: 300;
    font-size: 21px;
    color: var(--ink-grey);
    margin-bottom: 8px;
  }
  .contact-icon { width: 14px; height: 14px; flex: none; }

  /* Back */
  .card-back {
    background: var(--kivo-green);
    display: flex;
    flex-direction: column;
    align-items: center;
    justify-content: center;
    color: var(--card-white);
  }
  .back-name {
    font-family: "Lato", sans-serif;
    font-weight: 700;
    font-size: 150px;
    line-height: 1;
  }
  .back-tagline {
    font-family: "Lato", sans-serif;
    font-weight: 700;
    font-size: 26px;
    margin-top: 14px;
    letter-spacing: 0.5px;
  }
</style>
</head>
<body>

  <section class="card card-front" aria-label="Business card front">
    <div class="edge-band edge-band--top"></div>
    <div class="edge-rule edge-rule--top"></div>

    <div class="brand-name">Kivo</div>
    <div class="divider"></div>

    <div class="contact">
      <h1 class="contact-name">Dana Merritt</h1>
      <ul class="contact-list">
        <li class="contact-item">
          <svg class="contact-icon" viewBox="0 0 24 24" aria-hidden="true">
            <path fill="#37b553" d="M6.6 10.8c1.4 2.8 3.8 5.1 6.6 6.6l2.2-2.2c.3-.3.7-.4 1-.2 1.1.4 2.3.6 3.6.6.6 0 1 .4 1 1V20c0 .6-.4 1-1 1C10.6 21 3 13.4 3 4c0-.6.4-1 1-1h3.5c.6 0 1 .4 1 1 0 1.3.2 2.5.6 3.6.1.3 0 .7-.2 1z"/>
          </svg>
          (555) 014-2870
        </li>
        <li class="contact-item">
          <svg class="contact-icon" viewBox="0 0 24 24" aria-hidden="true">
            <rect x="2" y="5" width="20" height="14" rx="1" fill="#37b553"/>
            <path d="M3 6l9 7 9-7" fill="none" stroke="#fff" stroke-width="2"/>
          </svg>
          dana@kivocleaning.com
        </li>
        <li class="contact-item">
          <svg class="contact-icon" viewBox="0 0 24 24" aria-hidden="true">
            <circle cx="12" cy="12" r="9.5" fill="none" stroke="#37b553" stroke-width="2"/>
            <ellipse cx="12" cy="12" rx="4" ry="9.5" fill="none" stroke="#37b553" stroke-width="2"/>
            <path d="M2.5 12h19" stroke="#37b553" stroke-width="2"/>
          </svg>
          www.kivocleaning.com
        </li>
      </ul>
    </div>

    <div class="edge-rule edge-rule--bottom"></div>
    <div class="edge-band edge-band--bottom"></div>
  </section>

  <section class="card card-back" aria-label="Business card back">
    <div class="back-name">Kivo</div>
    <div class="back-tagline">commercial cleaning</div>
  </section>

</body>
</html>
```